Political Magazine & Corresponding Magazine Logo

I need a design for a monthly e-magazine that focuses on politics, public policy, as well as social, environmental, and economic justice. I would like a vibrant front and back cover, as well as internal pages that include a variety of design elements.

This magazine will be electronic ONLY and will not be published in print at this time.

I also need a logo design for the magazine that is attractive, includes the colors and images that communicate "authority" "trusted source", "professional", etc.

Industry/Entity Type

Political

Logo Text

Harborline Ember Review

Font styles to use
Serif
Sans Serif

Colors

Designer to choose colors to be used in the design.

Requirements
Must have
• I want the magazine design to include a variety of design elements that are consistent with the logo, as well as callouts, space for images, etc.
• I also need a logo design for the magazine that is attractive, includes the colors and images that communicate "authority" "trusted source", "professional", etc.
• I would like to have a color logo AND a white & black version of the same logo.
Nice to have
• I like various shades of navy blue.

```html
<!DOCTYPE html>
<html lang="en">
<head>
<meta charset="utf-8">
<title>Harborline Ember Review – Spread</title>
<link rel="stylesheet" href="https://fonts.googleapis.com/css2?family=Barlow:wght@400;500;600&display=swap">
<style>
  :root {
    --sky: #2a9fd8;
    --navy: #1a5ea8;
    --ink: #2f2f2f;
    --muted: #545454;
    --paper: #ffffff;
    --backdrop: #ececec;
    --photo-dark: #2c2a2c;
    --photo-warm: #6a4a38;
    --photo-teal: #3f8fae;
  }
  * { box-sizing: border-box; margin: 0; padding: 0; }
  html, body { width: 1200px; height: 888px; overflow: hidden; }
  body { background: var(--backdrop); font-family: "Barlow", sans-serif; position: relative; }

  .spread {
    position: absolute; left: 69px; top: 58px; width: 1064px; height: 757px;
    display: flex; background: var(--paper);
    box-shadow: 0 18px 30px rgba(0,0,0,.22);
  }
  .spread::before {
    content: ""; position: absolute; left: 0; right: 0; top: 43px; height: 2px;
    background: var(--sky); z-index: 2;
  }
  .page { position: relative; width: 532px; height: 757px; }
  .page--left { background: linear-gradient(90deg, #fff 80%, #f1f1f1 100%); border-right: 1px solid #dcdcdc; }
  .page--right { background: linear-gradient(90deg, #f3f3f3 0%, #fff 12%); }

  .running-head {
    position: absolute; top: 0; width: 261px; height: 45px;
    background: var(--sky); color: #fff;
    font-size: 15px; font-weight: 500; letter-spacing: -.2px;
    display: flex; align-items: center;
  }
  .page--left .running-head { left: 0; padding-left: 41px; }
  .page--right .running-head { left: 271px; padding-left: 42px; }

  .headline {
    position: absolute; left: 41px; top: 76px;
    font-size: 57px; line-height: 64px; font-weight: 600;
    color: var(--sky); letter-spacing: .5px;
  }
  .standfirst {
    position: absolute; left: 44px; top: 224px; width: 440px;
    font-size: 16.5px; line-height: 21.2px; color: var(--muted);
  }
  .hero-photo {
    position: absolute; left: 0; top: 362px; width: 532px; height: 324px;
    background: linear-gradient(135deg, #8fc7d8 0%, var(--photo-teal) 40%, #1e3f78 75%, #16203f 100%);
  }
  .folio {
    position: absolute; left: 246px; top: 721px; width: 40px; height: 36px;
    background: var(--sky); color: #fff; font-size: 12px;
    display: flex; align-items: center; justify-content: center;
  }

  .body-copy {
    font-size: 12.3px; line-height: 19.8px; color: var(--ink);
    text-align: justify; hyphens: auto; -webkit-hyphens: auto;
  }
  .column--narrow { position: absolute; left: 38px; top: 68px; width: 136px; letter-spacing: -.1px; }
  .column--narrow p + p { margin-top: 19.8px; }
  .event-photo {
    position: absolute; left: 194px; top: 73px; width: 298px; height: 216px;
    background: linear-gradient(160deg, #2a4f86 0%, var(--photo-dark) 45%, var(--photo-warm) 100%);
  }
  .pull-quote {
    position: absolute; left: 194px; top: 310px; width: 338px; height: 138px;
    background: var(--navy); color: #fff;
    padding: 20px 42px 0 29px;
    font-size: 14.6px; line-height: 19.8px; font-weight: 500; text-align: justify; letter-spacing: .3px;
    hyphens: auto; -webkit-hyphens: auto;
  }
  .column--wide { position: absolute; left: 194px; top: 465px; width: 298px; }
</style>
</head>
<body>
  <div class="spread">
    <section class="page page--left">
      <div class="running-head">HARBORLINE EMBER REVIEW</div>
      <h1 class="headline">LOREM IPSUM<br>DOLOR SIT AMET</h1>
      <p class="standfirst">Sed ut perspiciatis unde omnis iste natus error sit voluptatem accusantium doloremque laudantium, totam rem aperiam, eaque ipsa quae ab illo inventore veritatis et quasi architecto beatae vitae dicta sunt explicabo. Nemo enim ipsam voluptatem quia, sed quia consequu.</p>
      <div class="hero-photo" role="img" aria-label="Blue-toned collage photo of four women politicians speaking and waving at a rally"></div>
      <div class="folio">1</div>
    </section>

    <section class="page page--right">
      <div class="running-head">HARBORLINE EMBER REVIEW</div>
      <div class="column--narrow body-copy">
        <p>Lorem ipsum dolor sit amet, consectetur adipiscing elit, sed do eiusmod tempor inci&shy;didunt ut labore et dolore magna aliqua. Ut enim ad minim veniam, quis nostrud exercitation ullamco laboris nisi ut aliquip ex ea commodo consequat. Duis aute irure dolor in reprehen&shy;derit in voluptate velit esse cillum dolore eu fugiat nulla pariatur. Excepteur sint occaecat cupidatat non proident, sunt in culpa qui officia deserunt mollit anim id est laborum.</p>
        <p>Section 1.10.32 of "de Ratione Verbi et Sermonis", written by Varennius in 45 BC</p>
        <p>Sed ut perspiciatis unde omnis iste natus error sit voluptatem accusan&shy;tium doloremque laudantium, totam rem</p>
      </div>
      <div class="event-photo" role="img" aria-label="Photo of a panel discussion with women seated on a stage around a small table"></div>
      <blockquote class="pull-quote">Sed ut perspiciatis unde omnis iste natus error sit voluptatem accusan&shy;tium doloremque laudantium, totam rem aperiam, eaque ipsa quae ab illo inventore versunt explicabo.</blockquote>
      <div class="column--wide body-copy">
        <p>aperiam, eaque ipsa quae ab illo inventore veritatis et quasi architecto beatae vitae dicta sunt explicabo. Nemo enim ipsam voluptatem quia voluptas sit aspernatur aut odit aut fugit, sed quia consequuntur magni dolores eos qui ratione voluptatem sequi nesciunt. Neque porro quisquam est, qui dolorem ipsum quia dolor sit amet, consectetur, adipisci velit, sed quia non numquam eius modi tempora incidunt ut labore et dolore magnam aliquam quaerat voluptatem. Ut enim ad minima veniam, quis nostrum exercitationem ullam corporis suscipit laboriosam,</p>
      </div>
      <div class="folio">2</div>
    </section>
  </div>
</body>
</html>
```